Quimby's Yard & Garden Center Business Card Update

I need an updated Business card design for my Lawn and Garden Center. We do Landscaping installs, Lawn Mowing, Snow Removal and also have a Garden Center Retail Division. I uploaded a few of our previous business cards to give an idea of what we are starting with. The main goal of this update is to simplify and modernize the business card, not all of the services that are on the previous cards has to be on the new one but I would still like to highlight our main services. There is also a sample of our logo that Can be used in the design.

Industry/Entity Type

Landscaping

Contact Information for Business Card

Morris Quimby
Morris@Quimbysyardandgarden.example
Business (555) 201-7784
Cell (555) 318-6092

Colors

Designer to choose colors to be used in the design.

Requirements
Must have
• Services Provided :
• Landscaping
• Lawn Maintenance
• Snow Removal
• Garden Center

```html
<!DOCTYPE html>
<html lang="en">
<head>
<meta charset="utf-8">
<title>Quimby's Yard &amp; Garden Center – Business Card</title>
<link rel="stylesheet" href="https://fonts.googleapis.com/css2?family=Arimo:wght@400;700&family=Open+Sans:wght@700&display=swap">
<style>
  :root {
    --stage: #3a3a3a;
    --card: #ffffff;
    --green: #2a5224;
    --ink: #1c1c1c;
    --text: #3d3d3d;
    --photo-top: #eef2ec;
    --photo-mid: #dfe6da;
    --photo-low: #e9e6cf;
  }
  * { box-sizing: border-box; margin: 0; padding: 0; }
  html, body { width: 1200px; height: 1200px; overflow: hidden; }
  body {
    background: var(--stage);
    font-family: "Arimo", Arial, sans-serif;
    display: flex;
    flex-direction: column;
    align-items: center;
    justify-content: center;
    gap: 60px;
  }
  .card {
    position: relative;
    width: 840px;
    height: 480px;
    background: var(--card);
    overflow: hidden;
  }
  .brand {
    position: absolute;
    display: flex;
    align-items: center;
    gap: 12px;
    font-family: "Arimo", Arial, sans-serif;
    font-weight: 700;
    font-size: 54px;
    color: var(--green);
    white-space: nowrap;
  }
  .brand-dot {
    width: 38px; height: 38px;
    border-radius: 50%;
    background: var(--green);
    flex: none;
  }
  /* Back side */
  .card-back .photo {
    position: absolute; inset: 0;
    background: linear-gradient(180deg, var(--photo-top) 0%, var(--photo-top) 22%, var(--photo-mid) 55%, var(--photo-low) 100%);
  }
  .card-back .brand { left: 150px; top: 180px; }
  .services {
    position: absolute;
    left: 490px; top: 150px;
    color: var(--ink);
    white-space: nowrap;
  }
  .services-title {
    font-weight: 700;
    font-size: 26px;
    color: var(--green);
    margin-bottom: 14px;
  }
  .services-list { list-style: none; padding-left: 30px; }
  .services-list li { font-size: 24px; line-height: 34px; }
  .services-list li::before { content: "•"; margin-right: 8px; }
  /* Front side */
  .card-front .brand { left: 50px; top: 200px; }
  .divider {
    position: absolute;
    left: 368px; top: 120px;
    width: 2px; height: 230px;
    background: var(--green);
  }
  .contact { position: absolute; left: 392px; top: 140px; right: 20px; }
  .contact-name {
    font-family: "Open Sans", Arial, sans-serif;
    font-weight: 700;
    font-size: 30px;
    color: var(--green);
    text-transform: uppercase;
    margin: 0 0 26px 24px;
    white-space: nowrap;
  }
  .contact-list { list-style: none; }
  .contact-list li {
    display: flex; align-items: center; gap: 10px;
    font-size: 20px; line-height: 34px;
    color: var(--text);
    white-space: nowrap;
  }
  .contact-list svg { width: 18px; height: 18px; flex: none; fill: var(--green); }
</style>
</head>
<body>

<section class="card card-back">
  <div class="photo" role="img" aria-label="Faded photograph of the garden center storefront with greenhouse roof and potted mums"></div>
  <div class="brand"><span class="brand-dot"></span><span>Quimby's</span></div>
  <div class="services">
    <h2 class="services-title">Services Provided:</h2>
    <ul class="services-list">
      <li>Landscaping</li>
      <li>Lawn Maintenance</li>
      <li>Snow Removal</li>
      <li>Garden Center</li>
    </ul>
  </div>
</section>

<section class="card card-front">
  <div class="brand"><span class="brand-dot"></span><span>Quimby's</span></div>
  <div class="divider"></div>
  <div class="contact">
    <h1 class="contact-name">Morris Quimby</h1>
    <ul class="contact-list">
      <li>
        <svg viewBox="0 0 24 24" aria-hidden="true"><path d="M6.6 10.8a15.1 15.1 0 0 0 6.6 6.6l2.2-2.2a1 1 0 0 1 1-.25 11.4 11.4 0 0 0 3.6.57 1 1 0 0 1 1 1V20a1 1 0 0 1-1 1A17 17 0 0 1 3 4a1 1 0 0 1 1-1h3.5a1 1 0 0 1 1 1c0 1.25.2 2.45.57 3.57a1 1 0 0 1-.25 1z"/></svg>
        (555) 201-7784
      </li>
      <li>
        <svg viewBox="0 0 24 24" aria-hidden="true"><path d="M7 1h10a2 2 0 0 1 2 2v18a2 2 0 0 1-2 2H7a2 2 0 0 1-2-2V3a2 2 0 0 1 2-2zm0 3v15h10V4zm5 16.2a1 1 0 1 0 0 .01z"/></svg>
        (555) 318-6092
      </li>
      <li>
        <svg viewBox="0 0 24 24" aria-hidden="true"><path d="M2 5h20v14H2zm2 2v.5l8 5 8-5V7zm0 2.9V17h16V9.9l-8 5z"/></svg>
        Morris@Quimbysyardandgarden.example
      </li>
      <li>
        <svg viewBox="0 0 24 24" aria-hidden="true"><path d="M12 2a10 10 0 1 0 0 20 10 10 0 0 0 0-20zm6.9 6h-3a15 15 0 0 0-1.3-3.9A8 8 0 0 1 18.9 8zM12 4c.8 1.2 1.4 2.5 1.8 4h-3.6c.4-1.5 1-2.8 1.8-4zM4.3 14a8 8 0 0 1 0-4h3.4a16 16 0 0 0 0 4zm.8 2h3a15 15 0 0 0 1.3 3.9A8 8 0 0 1 5.1 16zm3-8h-3a8 8 0 0 1 4.3-3.9A15 15 0 0 0 8.1 8zM12 20c-.8-1.2-1.4-2.5-1.8-4h3.6c-.4 1.5-1 2.8-1.8 4zm2.3-6H9.7a14 14 0 0 1 0-4h4.6a14 14 0 0 1 0 4zm.3 5.9a15 15 0 0 0 1.3-3.9h3a8 8 0 0 1-4.3 3.9zM16.3 14a16 16 0 0 0 0-4h3.4a8 8 0 0 1 0 4z"/></svg>
        www.quimbysyardandgarden.example
      </li>
    </ul>
  </div>
</section>

</body>
</html>
```